Flyer-Design für ambulanten Pflegedienst
Zielgruppe
Wir sind ein ambulanter Pflegedienst im Raum Rostock und Gnoien. Patienten werden in der Häuslichkeit versorgt.
Aufgabenstellung
Überschrift: Der Pflegedienst im Herzen von Rostock
Der Faltflyer sollte darüber aufklären, dass Leistungen der Behandlungspflege von der Krankenkasse übernommen werden. Dazu zählt die Medikamentengabe das anziehen von Kompressionsstrümpfen und die Insulininjektion. Darüber soll in dem Flyer aufgeklärt werden. Die Texte können den Postkarten Flyern entnommen werden.
Der Flyer sollte einen hochwertigen Eindruck machen und
nicht zu viel Text enthalten. Da wir zwei ambulante Pflegedienste betreiben, soll der Flyer im Impressum mit zwei verschiedenen Adressen und zwei verschiedenen Logos auf der Rückseite erstellt werden.
Der Slogan des Flyers sollte sein: Der Pflegedienst im Herzen von Rostock.

```html
<!DOCTYPE html>
<html lang="de">
<head>
<meta charset="utf-8">
<title>Faltflyer Pflegehof Küste</title>
<link href="https://fonts.googleapis.com/css2?family=Quicksand:wght@500;700&family=Short+Stack&display=swap" rel="stylesheet">
<style>
:root{
  --green:#86cf6f;
  --green-light:#a9de8f;
  --green-dark:#5fb548;
  --blue:#1b73c2;
  --blue-dark:#0f5ea8;
  --orange:#f2a445;
  --orange-light:#f7c277;
  --ink:#1f5fa6;
  --grey:#eef0f3;
  --paper:#ffffff;
  --stage:#ececec;
}
*{box-sizing:border-box;margin:0;padding:0}
html,body{width:834px;height:1200px;overflow:hidden}
body{background:var(--stage);font-family:"Quicksand",sans-serif;color:var(--ink);position:relative}
.spread{position:absolute;left:37px;width:760px;height:520px;box-shadow:0 10px 28px rgba(0,0,0,.15);overflow:hidden;background:var(--paper)}
.spread--outside{top:50px}
.spread--inside{top:630px}
.panel{position:absolute;top:0;width:380px;height:520px;overflow:hidden}
.panel--left{left:0}
.panel--right{left:380px}
.abs{position:absolute}
.hand{font-family:"Short Stack",cursive}

/* back panel */
.back{background:linear-gradient(160deg,var(--green-light),var(--green) 60%,var(--green-dark))}
.brand{display:flex;align-items:center;gap:8px;color:#fff;font-weight:700}
.brand-dot{width:34px;height:34px;border-radius:50%;border:3px solid #fff}
.brand-name{font-size:19px}
.contact{color:#fff;font-size:9px;line-height:1.35;display:flex;gap:8px;align-items:flex-start;margin-bottom:9px}
.contact svg{flex:none;width:14px;height:14px}
.url-pill{display:inline-block;background:var(--blue);color:#fff;font-weight:700;font-size:10px;padding:5px 14px;border-radius:12px;letter-spacing:.3px}
.sub{font-size:7px;color:#fff;font-weight:700;margin-top:2px}

/* front panel */
.front-headline{left:24px;top:378px;width:340px;font-size:27px;line-height:1.15;color:#fff;letter-spacing:.5px}
.front-url{left:70px;top:462px;background:var(--orange);color:#fff;font-weight:700;font-size:12px;padding:7px 20px;border-radius:16px}
.badge{border-radius:50%;background:var(--orange);border:3px solid var(--orange-light);color:#fff;text-align:center;display:flex;flex-direction:column;justify-content:center;align-items:center;font-size:9px;line-height:1.2}
.badge b{font-weight:700;font-size:10px}
.front-brand{left:20px;top:28px;color:var(--ink)}
.front-brand .brand-dot{border-color:var(--blue)}
.front-brand .brand-name{color:var(--green-dark)}

/* inside */
.inside-top{left:0;top:0;width:760px;height:250px;background:linear-gradient(180deg,#e4e8ee,#f3f5f7 80%,#fff)}
.tag{display:inline-block;color:#fff;font-size:13px;padding:3px 14px;border-radius:12px;margin-bottom:4px}
.tag--green{background:var(--green)}
.tag--orange{background:var(--orange)}
.phone-pill{background:var(--blue);color:#fff;font-size:15px;padding:4px 16px;border-radius:14px;display:inline-flex;gap:8px;align-items:center}
.phone-note{font-size:7px;text-align:center;color:var(--ink);margin-top:2px}
.section-title{display:inline-block;background:var(--green);color:#fff;font-size:14px;padding:4px 16px;border-radius:14px}
.lead{font-weight:700;font-size:9.5px;margin:8px 0 6px}
.body{font-size:8px;line-height:1.4;margin-bottom:6px}
.req{font-weight:700;font-size:8.5px;margin:4px 0 3px}
.ticks{list-style:none;font-size:8px;line-height:1.35}
.ticks li{display:flex;gap:5px;margin-bottom:3px}
.ticks svg{flex:none;width:9px;height:9px;margin-top:2px}
.bottom-band{left:0;bottom:0;width:760px;height:10px;background:var(--blue)}
.fold{left:379px;top:0;width:1px;height:520px;background:rgba(0,0,0,.08)}
</style>
</head>
<body>

<!-- Outside spread -->
<section class="spread spread--outside">
  <div class="panel panel--left back">
    <div class="abs brand" style="left:118px;top:40px">
      <span class="brand-dot"></span><span class="brand-name">Pflegehof Küste</span>
    </div>
    <div class="abs" style="left:70px;top:110px;width:280px">
      <div class="contact"><svg viewBox="0 0 14 14"><path d="M7 1a4 4 0 0 0-4 4c0 3 4 8 4 8s4-5 4-8a4 4 0 0 0-4-4z" fill="#fff"/><circle cx="7" cy="5" r="1.5" fill="var(--green)"/></svg><span>Pflegehof Küste GmbH<br>Lindenweg 7 | 18055 Rostock</span></div>
      <div class="contact"><svg viewBox="0 0 14 14"><path d="M3 1l3 3-1.5 2a8 8 0 0 0 3.5 3.5L10 8l3 3-2 2C6 13 1 8 1 3z" fill="#fff"/></svg><span>Telefon:<br>0381-5550142</span></div>
      <div class="contact"><svg viewBox="0 0 14 14"><rect x="1" y="3" width="12" height="8" rx="1" fill="#fff"/><path d="M1.5 3.5L7 8l5.5-4.5" stroke="var(--green)" fill="none"/></svg><span>E-Mail:<br>info@pflegehof-kueste.de</span></div>
      <span class="url-pill">www.pflegehof-kueste.de</span>
    </div>
    <div class="abs brand" style="left:118px;top:290px">
      <span class="brand-dot" style="border-radius:4px"></span>
      <div><div class="brand-name">MOVACARE</div><div class="sub">Der Mobile Pflegedienst</div></div>
    </div>
    <div class="abs" style="left:70px;top:355px;width:280px">
      <div class="contact"><svg viewBox="0 0 14 14"><path d="M7 1a4 4 0 0 0-4 4c0 3 4 8 4 8s4-5 4-8a4 4 0 0 0-4-4z" fill="#fff"/><circle cx="7" cy="5" r="1.5" fill="var(--green)"/></svg><span>Filiale Gnoien<br>Ahornstraße 12 | 17179 Gnoien</span></div>
      <div class="contact"><svg viewBox="0 0 14 14"><path d="M3 1l3 3-1.5 2a8 8 0 0 0 3.5 3.5L10 8l3 3-2 2C6 13 1 8 1 3z" fill="#fff"/></svg><span>Telefon:<br>039971 555210</span></div>
      <div class="contact"><svg viewBox="0 0 14 14"><rect x="1" y="3" width="12" height="8" rx="1" fill="#fff"/><path d="M1.5 3.5L7 8l5.5-4.5" stroke="var(--green)" fill="none"/></svg><span>E-Mail:<br>info@movacare.de</span></div>
      <span class="url-pill">www.movacare.de</span>
    </div>
  </div>

  <div class="panel panel--right">
    <svg class="abs" width="380" height="520" viewBox="0 0 380 520" style="left:0;top:0">
      <rect width="380" height="8" fill="var(--green-light)"/>
      <rect y="190" width="380" height="330" fill="var(--blue)"/>
      <circle cx="215" cy="205" r="160" fill="#fff"/>
    </svg>
    <div class="abs" role="img" aria-label="Foto: Pflegerin umarmt lächelnde Seniorin im Rollstuhl im Grünen" style="left:65px;top:63px;width:290px;height:290px;border-radius:50%;background:radial-gradient(circle at 40% 40%,#f1ece6,#d9dfe6 55%,#a9bda0)"></div>
    <div class="abs brand front-brand"><span class="brand-dot"></span><span class="brand-name">Pflegehof Küste</span></div>
    <div class="abs badge" style="left:278px;top:70px;width:92px;height:92px"><b>KRANKEN-<br>KASSEN</b>bezahlen die<b>LEISTUNGEN</b>für Sie!</div>
    <div class="abs hand front-headline">DER PFLEGEDIENST IM HERZEN VON ROSTOCK</div>
    <div class="abs front-url">www.pflegehof-kueste.de</div>
  </div>
</section>

<!-- Inside spread -->
<section class="spread spread--inside">
  <div class="abs inside-top"></div>
  <div class="abs" role="img" aria-label="Foto: Insulinpen, Teststreifen und Blutzuckermessgerät auf einem Messprotokoll" style="left:20px;top:-60px;width:270px;height:270px;border-radius:50%;background:radial-gradient(circle at 50% 55%,#f7f8fa,#d7dde5 60%,#9fb0c8)"></div>
  <div class="abs" role="img" aria-label="Foto: Hände ziehen einen Kompressionsstrumpf über einen Fuß" style="left:520px;top:20px;width:220px;height:220px;border-radius:50%;background:radial-gradient(circle at 45% 55%,#f6dccb,#e8bfa5 60%,#a77d62)"></div>
  <div class="abs badge" style="left:670px;top:180px;width:80px;height:80px;font-size:8px">nach den neuesten, fachlichen Erkenntnissen</div>

  <div class="abs hand" style="left:290px;top:70px;width:200px;text-align:center">
    <span class="tag tag--green">PFLEGE BEDEUTET</span><br>
    <span class="tag tag--green">VERANTWORTUNG!</span><br>
    <span class="tag tag--orange">WIR KÜMMERN UNS UM SIE</span>
    <div style="margin-top:10px">
      <span class="phone-pill"><svg width="12" height="12" viewBox="0 0 14 14"><path d="M3 1l3 3-1.5 2a8 8 0 0 0 3.5 3.5L10 8l3 3-2 2C6 13 1 8 1 3z" fill="#fff"/></svg>0800 55501 77</span>
      <div class="phone-note">(KOSTENFREI)</div>
    </div>
  </div>

  <div class="abs" style="left:28px;top:245px;width:320px">
    <span class="section-title hand">INSULININJEKTION</span>
    <div class="lead">Wir helfen Ihnen bei Insulin-Injektionen</div>
    <p class="body">Sollten Sie oder Ihre Angehörigen einen Hilfebedarf bei behandlungspflegerischen Leistungen haben, setzen wir uns gerne mit Ihrem Hausarzt in Verbindung. Dies ist selbstverständlich ein kostenloser Service des Mobilen Pflegedienstes PFLEGEHOF-KÜSTE.</p>
    <div class="req">Voraussetzungen sind:</div>
    <ul class="ticks">
      <li><svg viewBox="0 0 10 10"><path d="M1 5l3 3 5-6" stroke="var(--green)" stroke-width="2" fill="none"/></svg>Es muss eine behandlungsbedürftige Erkrankung vorliegen</li>
      <li><svg viewBox="0 0 10 10"><path d="M1 5l3 3 5-6" stroke="var(--green)" stroke-width="2" fill="none"/></svg>Ein Arzt muss eine Verordnung auf Behandlungspflege ausstellen</li>
      <li><svg viewBox="0 0 10 10"><path d="M1 5l3 3 5-6" stroke="var(--green)" stroke-width="2" fill="none"/></svg>Sie selbst oder eine Person in Ihrem Haushalt sind nicht in der Lage, die Leistung auszuführen, beispielsweise eine Insulininjektion oder das Anziehen von Kompressionsstrümpfen.</li>
    </ul>
    <p class="body" style="margin-top:6px">Behandlungspflegen (z.B. Injektionen, Verbandswechsel) sind gleichzeitig neben Leistungen der Pflegeversicherung möglich. Wenn Sie Leistungen der Behandlungspflege in Anspruch nehmen, wird das Pflegegeld nicht gekürzt.</p>
  </div>

  <div class="abs" style="left:405px;top:265px;width:330px">
    <span class="section-title hand">KOMPRESSIONSSTRÜMPFE</span>
    <div class="lead">Wir helfen Ihnen beim Anziehen von Kompressionsstrümpfen</div>
    <p class="body">Unter dem Begriff „Behandlungspflege“ sind all diejenigen Tätigkeiten zusammengefasst, die zur Behandlung/Therapie einer Krankheit notwendig sind und durch Ihren Hausarzt verordnet werden.</p>
    <div class="req">Sie umfasst folgende Hilfeleistungen:</div>
    <ul class="ticks">
      <li><svg viewBox="0 0 10 10"><path d="M1 5l3 3 5-6" stroke="var(--green)" stroke-width="2" fill="none"/></svg>Die Gabe von Medikamenten</li>
      <li><svg viewBox="0 0 10 10"><path d="M1 5l3 3 5-6" stroke="var(--green)" stroke-width="2" fill="none"/></svg>An- und Ausziehen von Kompressionsstrümpfen</li>
      <li><svg viewBox="0 0 10 10"><path d="M1 5l3 3 5-6" stroke="var(--green)" stroke-width="2" fill="none"/></svg>Injektionen, Verbände, Wund- und Dekubitus Versorgung</li>
    </ul>
    <p class="body" style="margin-top:6px">Die notwendigen verordneten und bewilligten Leistungen der Behandlungspflege werden von den Krankenkassen komplett finanziert bist auf die gesetzlich festgelegten Zahlungen.</p>
    <p class="body">Wenn Sie von der Zahlung befreit sind, müssen Sie zur Behandlungspflege nichts zahlen.</p>
  </div>

  <div class="abs fold"></div>
  <div class="abs bottom-band"></div>
</section>

</body>
</html>
```